We need an eye catching logo design and Business Card that portrays our business, which is the cleaning and protecting of stainless steel with an organic non chemical product. This can be separate to the company name or can incorporate it. Maybe even just the company name itself. Company Name is Gleamwise Gleamwise.
Ideal for products exposed to weather elements, ie: balustrading, enclosures, BBQs, we also supply the product so you can do it yourself (DIY).
In addition we would want to include on this card:
1. My Name (Paul Dremmick)
2. Mobile No. (TBA Later)
3. Email address (TBA Later)
4. Web address (TBA Later)
Updates

Please note that we also need suggestions on a logo, as this we do not have this either.

Please note we have update our brief to be more specific.

Thank You.

Paul

Reason: Awaiting for a couple of revised submissions from feedback given.

Target Market(s)

Purchasing officers and government people.

Industry/Entity Type

Steel

Colors

Designer to choose colors to be used in the design.

Requirements
Must have
• 1. Name (Paul Dremmick)
2. Mobile No. (TBA Later)
Should not have
• Should not be to busy looking

```html
<!DOCTYPE html>
<html lang="en">
<head>
<meta charset="utf-8">
<title>Gleamwise Gleamwise – Paul Dremmick</title>
<link href="https://fonts.googleapis.com/css2?family=Bebas+Neue&family=Montserrat:wght@400&display=swap" rel="stylesheet">
<style>
  :root {
    --steel-light: #e4ecec;
    --steel-mid: #b9c6c7;
    --steel-dark: #8fa1a3;
    --ink-deep: #1d3436;
    --ink-teal: #4d7074;
    --ink-contact: #2e3c3e;
  }
  html, body {
    margin: 0;
    padding: 0;
    width: 1200px;
    height: 796px;
    overflow: hidden;
    background: #ffffff;
  }
  .business-card {
    position: relative;
    width: 1200px;
    height: 796px;
    overflow: hidden;
    background:
      repeating-linear-gradient(0deg, rgba(255,255,255,0.07) 0 1px, rgba(0,0,0,0.03) 1px 3px),
      radial-gradient(ellipse 70% 55% at 78% 28%, rgba(255,255,255,0.55), rgba(255,255,255,0) 70%),
      linear-gradient(100deg, var(--steel-dark) 0%, var(--steel-mid) 35%, var(--steel-light) 70%, var(--steel-mid) 100%);
  }
  .company-name {
    position: absolute;
    left: 56px;
    top: 64px;
    margin: 0;
    font-family: "Bebas Neue", sans-serif;
    font-weight: 400;
    font-size: 96px;
    line-height: 1;
    letter-spacing: 1px;
    color: var(--ink-deep);
    white-space: nowrap;
  }
  .company-name .second-word { color: var(--ink-teal); }
  .person-name {
    position: absolute;
    left: 52px;
    top: 330px;
    margin: 0;
    font-family: "Bebas Neue", sans-serif;
    font-weight: 400;
    font-size: 142px;
    line-height: 1;
    letter-spacing: 2px;
    color: var(--ink-deep);
    text-shadow: 0 1px 0 rgba(255,255,255,0.45);
    white-space: nowrap;
  }
  .contact-list {
    position: absolute;
    left: 56px;
    top: 486px;
    margin: 0;
    padding: 0;
    list-style: none;
    font-family: "Montserrat", sans-serif;
    font-size: 54px;
    line-height: 76px;
    color: var(--ink-contact);
    white-space: nowrap;
  }
  .website {
    position: absolute;
    left: 0;
    width: 1200px;
    top: 700px;
    margin: 0;
    text-align: center;
    font-family: "Montserrat", sans-serif;
    font-size: 50px;
    line-height: 1;
    color: var(--ink-contact);
    padding-left: 4px;
  }
</style>
</head>
<body>
  <main class="business-card">
    <h1 class="company-name">Gleamwise <span class="second-word">Gleamwise</span></h1>
    <h2 class="person-name">Paul Dremmick</h2>
    <ul class="contact-list">
      <li class="contact-phone">T: +61 4821 9037</li>
      <li class="contact-email">E: paul@gleamwise.com</li>
    </ul>
    <p class="website">www.gleamwisegleamwise.com</p>
  </main>
</body>
</html>
```